Retail healthy snack bar design

We are launching a new product range to be sold in health food stores.

The Fennick Co (no logo as yet).

We will have a range of bars, spreads (jars), shakes (bags) in the following ranges-
milk protein
plant protein
keto

For this project, please do a bar design. The chosen designer will be given additional work for the rest of the packaging as well as promotional material such as social media, banners, posters etc.

Lumo Bar Protein - Must be White to be recognized.
Lumo Bar Collagen - Bronze
Lumo Keto Bar - Possibly Red
Lumo Bar Plant - Green

Food images can be added but their must be samples without as we may need to remove for certain countries.

Target Market(s)

Healthy, Weight-loss, Bodybuilding, Elderly, Medical

Industry/Entity Type

Health And Wellness

Font styles to use
Sans Serif

Colors

Designer to choose colors to be used in the design.

Requirements
Must have
• Clean simple to read design with minimal colours

Flavour to be easily read (Must include the word 'Flavour' in the same size font as the flavour description)

Must show size of bar (60g).

Some details that can be added (optional)-
raw, cold pressed bar with (example) whey protein isolate + prebiotic fibre
natural, with no artificial colours, flavours, preservatives or sweeteners
no added sugar or sugar alcohols - gluten free - soy free

Rear of bar shall remain the same or all same details if redesigned.
Nice to have
• Clean design, use of silver foil and/or matt/gloss affect, large oversized flavour image (if including).

See images of current designs I like on the market for ideas
Should not have
• Too many images (if any).

```html
<!DOCTYPE html>
<html lang="en">
<head>
<meta charset="utf-8">
<title>Lumo Bar Protein – Banana Bread Flavour wrapper</title>
<link rel="stylesheet" href="https://fonts.googleapis.com/css2?family=Montserrat:wght@800;900&family=Oswald:wght@300;400;500&display=swap">
<style>
  :root {
    --bg: #e8eae5;
    --gold: #f2b84a;
    --gold-deep: #e5a232;
    --gold-text: #e9a23a;
    --ink: #141414;
    --paper: #fbfbfa;
    --silver-light: #f1f1f1;
    --silver-dark: #9c9c9c;
    --grey-text: #555;
  }
  * { box-sizing: border-box; margin: 0; padding: 0; }
  html, body { width: 1200px; height: 942px; overflow: hidden; }
  body { background: var(--bg); position: relative; font-family: "Oswald", sans-serif; }

  .wrapper {
    position: absolute; left: 50px; top: 321px;
    width: 1100px; height: 300px;
    filter: drop-shadow(0 14px 18px rgba(0,0,0,.18));
  }
  .wrapper__shape { position: absolute; inset: 0; }

  .brand {
    position: absolute; left: 132px; top: 12px;
    font-family: "Montserrat", sans-serif; font-weight: 900;
    font-size: 154px; line-height: 1; letter-spacing: -4px;
    color: var(--ink);
  }
  .product-type {
    position: absolute; left: 134px; top: 160px;
    font-weight: 300; font-size: 60px; line-height: 1; letter-spacing: 3px;
    color: var(--ink);
  }
  .net-weight {
    position: absolute; left: 132px; top: 240px;
    width: 192px; height: 36px; border-radius: 18px;
    background: linear-gradient(180deg, #fdfdfd, #b9b9b9 55%, #e4e4e4);
    box-shadow: 0 2px 3px rgba(0,0,0,.25);
    font-weight: 500; font-size: 17px; line-height: 36px; text-align: center;
    color: var(--ink);
  }

  .flavour-band {
    position: absolute; left: 766px; top: 38px;
    width: 296px; height: 94px;
    background: var(--ink); border-radius: 47px 0 0 47px;
    overflow: hidden;
  }
  .flavour-image {
    position: absolute; left: 14px; top: 9px;
    width: 76px; height: 76px; border-radius: 50%;
    background: radial-gradient(circle at 45% 40%, #f5c35a, #c98d22 70%, #3a2c12);
  }
  .flavour-name {
    position: absolute; left: 114px; top: 13px;
    font-family: "Montserrat", sans-serif; font-weight: 800; line-height: 1;
  }
  .flavour-name__line1 { display: block; font-size: 26px; color: var(--paper); }
  .flavour-name__line2 { display: block; font-size: 33px; color: var(--gold-text); margin-top: 1px; }
  .flavour-name__label {
    display: block; font-family: "Oswald", sans-serif; font-weight: 300;
    font-size: 13px; letter-spacing: 9px; color: #bdbdbd; margin-top: 4px;
  }

  .claim {
    position: absolute; top: 162px;
    font-weight: 300; font-size: 17px; line-height: 1.2; color: var(--ink);
    text-transform: uppercase;
  }
  .claim--natural { left: 480px; }
  .claim--raw { right: 62px; text-align: right; }

  .badge-row { position: absolute; left: 498px; top: 208px; width: 370px; height: 80px; }
  .badge-row__line { position: absolute; left: 28px; right: 40px; top: 29px; height: 3px; background: var(--gold); }
  .badge {
    position: absolute; top: 0; width: 58px; text-align: center;
  }
  .badge__icon { display: block; width: 58px; height: 58px; }
  .badge__label { display: block; margin-top: 4px; font-size: 11px; color: var(--grey-text); white-space: nowrap; margin-left: -10px; margin-right: -10px; }

  .protein-box {
    position: absolute; left: 924px; top: 214px;
    width: 114px; height: 62px;
    border: 3px solid var(--gold); border-radius: 7px;
    text-align: center; overflow: hidden;
  }
  .protein-box__top { display: block; font-size: 17px; line-height: 28px; color: var(--gold-text); }
  .protein-box__bottom {
    display: block; margin: 0 4px; border-radius: 4px;
    background: var(--gold); color: var(--paper);
    font-size: 16px; line-height: 24px;
  }
</style>
</head>
<body>
  <div class="wrapper">
    <svg class="wrapper__shape" width="1100" height="300" viewBox="0 0 1100 300">
      <defs>
        <linearGradient id="silver" x1="0" y1="0" x2="0" y2="1">
          <stop offset="0" stop-color="#f3f3f3"/>
          <stop offset="0.5" stop-color="#a6a6a6"/>
          <stop offset="1" stop-color="#dedede"/>
        </linearGradient>
      </defs>
      <path class="crimp-left" fill="#e8ad40" d="M40 0 L0 0 L8 12 L0 24 L8 36 L0 48 L8 60 L0 72 L8 84 L0 96 L8 108 L0 120 L8 132 L0 144 L8 156 L0 168 L8 180 L0 192 L8 204 L0 216 L8 228 L0 240 L8 252 L0 264 L8 276 L0 288 L8 300 L40 300 Z"/>
      <rect x="40" y="0" width="420" height="300" fill="var(--gold)"/>
      <rect x="460" y="0" width="602" height="300" fill="var(--paper)"/>
      <path class="crimp-right" fill="url(#silver)" d="M1062 0 L1100 0 L1092 12 L1100 24 L1092 36 L1100 48 L1092 60 L1100 72 L1092 84 L1100 96 L1092 108 L1100 120 L1092 132 L1100 144 L1092 156 L1100 168 L1092 180 L1100 192 L1092 204 L1100 216 L1092 228 L1100 240 L1092 252 L1100 264 L1092 276 L1100 288 L1092 300 L1062 300 Z"/>
    </svg>

    <div class="brand">LUMO</div>
    <div class="product-type">PROTEIN BAR</div>
    <div class="net-weight">NET WT. 2.12 OZ (60G)</div>

    <div class="flavour-band">
      <div class="flavour-image" role="img" aria-label="Illustration of a peeled banana"></div>
      <div class="flavour-name">
        <span class="flavour-name__line1">BANANA</span>
        <span class="flavour-name__line2">BREAD</span>
        <span class="flavour-name__label">FLAVOUR</span>
      </div>
    </div>

    <p class="claim claim--natural">Natural, with no artificial colors,<br>flavours or preservatives</p>
    <p class="claim claim--raw">Raw, cold pressed whey protein<br>isolate + prebiotic fibre</p>

    <div class="badge-row">
      <div class="badge-row__line"></div>
      <div class="badge" style="left:0">
        <svg class="badge__icon" viewBox="0 0 58 58"><circle cx="29" cy="29" r="26" fill="#fff" stroke="var(--gold)" stroke-width="3"/><ellipse cx="29" cy="23" rx="12" ry="5" fill="none" stroke="#777" stroke-width="2"/><path d="M17 23 V35 Q29 42 41 35 V23" fill="none" stroke="#777" stroke-width="2"/></svg>
        <span class="badge__label">Low Fat</span>
      </div>
      <div class="badge" style="left:78px">
        <svg class="badge__icon" viewBox="0 0 58 58"><circle cx="29" cy="29" r="26" fill="#fff" stroke="var(--gold)" stroke-width="3"/><rect x="16" y="22" width="26" height="14" rx="7" fill="none" stroke="#777" stroke-width="2"/><line x1="17" y1="41" x2="41" y2="17" stroke="#777" stroke-width="2"/></svg>
        <span class="badge__label">Low Carb</span>
      </div>
      <div class="badge" style="left:156px">
        <svg class="badge__icon" viewBox="0 0 58 58"><circle cx="29" cy="29" r="26" fill="#fff" stroke="var(--gold)" stroke-width="3"/><path d="M29 17 L40 23 V35 L29 41 L18 35 V23 Z M18 23 L29 29 L40 23 M29 29 V41" fill="none" stroke="#777" stroke-width="2"/><line x1="17" y1="41" x2="41" y2="17" stroke="#777" stroke-width="2"/></svg>
        <span class="badge__label">No Added Sugar</span>
      </div>
      <div class="badge" style="left:234px">
        <svg class="badge__icon" viewBox="0 0 58 58"><circle cx="29" cy="29" r="26" fill="#fff" stroke="var(--gold)" stroke-width="3"/><line x1="29" y1="16" x2="29" y2="42" stroke="#777" stroke-width="2"/><path d="M29 24 L23 20 M29 24 L35 20 M29 31 L23 27 M29 31 L35 27" stroke="#777" stroke-width="2"/><line x1="17" y1="41" x2="41" y2="17" stroke="#777" stroke-width="2"/></svg>
        <span class="badge__label">Gluten free</span>
      </div>
      <div class="badge" style="left:312px">
        <svg class="badge__icon" viewBox="0 0 58 58"><circle cx="29" cy="29" r="26" fill="#fff" stroke="var(--gold)" stroke-width="3"/><rect x="17" y="23" width="24" height="12" rx="6" fill="none" stroke="#777" stroke-width="2" transform="rotate(-40 29 29)"/><circle cx="25" cy="33" r="2.5" fill="#777"/><circle cx="33" cy="25" r="2.5" fill="#777"/></svg>
        <span class="badge__label">Soy Free</span>
      </div>
    </div>

    <div class="protein-box">
      <span class="protein-box__top">OVER 20G</span>
      <span class="protein-box__bottom">PROTEIN</span>
    </div>
  </div>
</body>
</html>
```